Lawn Company needs design work on a service call flyer!

We are a lawn care company that fertilizes and sprays lawns. This design is meant to be left behind at the customers house after a lawn application has been done too let them know what we have done.

The finished design will be printed on A6 paper (4.1 x 5.8 inches)

I have attached PDF files of the text that I want on the front of the document and the back of the document. I also included a sample design that I had been working on to give some idea what I would like. I don't want the same design, but you can use it as a building block for something new or come up with something entirely different.

FRONT: The front of the design is most important.

BACK: Other then the text the design should be minimal. If possible I would like an outline of the trees in my logo to be a backdrop. I have attached a PDF of the back of my business card as an example

The winning design will be a professional looking document that flows and reflects a lawn care business. Please contact me if you have any questions. I will only pick a design that is better then my current template.

Thank You

Target Market(s)

Lawn Care Customers

Industry/Entity Type

Lawn Care

Requirements
Must have
• 1. Our Logo
• 2. The attached text for the front & back of document
• 3. Our phone number (604-918-4471)
• 4. Our Email address (fenwickturfcare@mailora.net)
Nice to have
• A green theme with flowing graphics
Should not have
• any pictures of houses, people, or tools
• Don't copy the text or design from my design template. It is outdated, is it meant to be an example only

```html
<!DOCTYPE html>
<html lang="en">
<head>
<meta charset="utf-8">
<title>Fenwick Turf Care – Service Call Flyer</title>
<link rel="stylesheet" href="https://fonts.googleapis.com/css2?family=Lato:ital,wght@0,400;0,700;0,900;1,700&display=swap">
<style>
  :root {
    --ink: #222222;
    --white: #ffffff;
    --brand-green: #3b8a22;
    --tree-dark: #2e6a1c;
    --tree-light: #7cbf49;
  }
  html, body {
    margin: 0;
    padding: 0;
    background: var(--white);
    overflow: hidden;
  }
  .flyer {
    position: relative;
    width: 813px;
    height: 1200px;
    overflow: hidden;
    background: var(--white);
    font-family: "Lato", Arial, sans-serif;
    color: var(--ink);
  }
  .abs { position: absolute; margin: 0; }

  .application-date {
    top: 8px; left: 470px;
    font-size: 13px; letter-spacing: .5px;
  }
  .application-date .fill-line {
    display: inline-block; width: 150px;
    border-bottom: 1px solid var(--ink); vertical-align: -2px;
  }
  .serviced-heading {
    top: 30px; left: 48px;
    font-size: 14px; font-weight: 700; letter-spacing: .4px;
  }
  .consists {
    top: 62px; left: 48px;
    font-size: 14px; font-weight: 700;
  }
  .treatment-list {
    top: 100px; left: 48px;
    list-style: none; padding: 0;
    font-size: 14px; font-weight: 700;
  }
  .treatment-list li { height: 44px; }
  .treatment-list .marker { display: inline-block; width: 36px; font-weight: 400; }
  .treatment-list .fill-line {
    display: inline-block; width: 70px;
    border-bottom: 1px solid var(--ink); vertical-align: -2px;
  }
  .watering-note {
    top: 278px; left: 48px;
    font-size: 14px;
  }
  .watering-note .fill-line {
    display: inline-block; width: 100px;
    border-bottom: 1px solid var(--ink); vertical-align: -2px;
  }
  .promise {
    top: 316px; left: 48px; width: 720px;
    font-size: 13.5px; font-weight: 700; font-style: italic; line-height: 1.3;
  }

  .lawn-band { top: 400px; left: 0; width: 813px; height: 275px; }
  .tree-artwork {
    top: 428px; left: 44px; width: 150px; height: 148px;
    border-radius: 50% 50% 12px 12px;
    background: radial-gradient(circle at 50% 35%, var(--tree-light), var(--tree-dark));
  }
  .brand-name {
    top: 578px; left: 30px;
    font-size: 44px; font-weight: 900; letter-spacing: 1px; line-height: 1;
    color: var(--white);
  }
  .brand-tagline {
    top: 626px; left: 34px;
    font-size: 21px; font-weight: 900; letter-spacing: 2px;
    color: var(--white);
  }
  .contact-phone {
    top: 548px; right: 46px;
    font-size: 30px; color: var(--brand-green); letter-spacing: 1px;
  }
  .contact-email {
    top: 594px; right: 40px;
    font-size: 21px; color: var(--brand-green);
  }

  .care-guide {
    top: 702px; left: 30px; width: 752px;
    font-size: 11.5px; line-height: 1.45;
  }
  .care-guide p { margin: 0; }
  .care-guide .section-title { font-weight: 700; }
  .care-guide .section-lead { margin-bottom: 20px; }
  .care-guide ul { list-style: none; padding: 0; margin: 0 0 16px; }
  .care-guide li { position: relative; padding-left: 20px; margin-bottom: 24px; }
  .care-guide li:last-child { margin-bottom: 0; }
  .care-guide li::before { content: "-"; position: absolute; left: 4px; }
</style>
</head>
<body>
<div class="flyer">

  <p class="abs application-date">APPLICATION TIME / DATE: <span class="fill-line"></span></p>

  <p class="abs serviced-heading">YOUR LAWN HAS BEEN PROFESSIONALLY SERVICED TODAY BY</p>
  <p class="abs consists">Today's application consists of</p>
  <ul class="abs treatment-list">
    <li><span class="marker">o</span>Seasonally Balanced Slow Release Fertilizer</li>
    <li><span class="marker">o</span>Broadleaf Weed Control (Please keep off the lawn until it is thoroughly dry)</li>
    <li><span class="marker">o</span>Other <span class="fill-line"></span></li>
  </ul>

  <p class="abs watering-note">Please begin watering the lawn <span class="fill-line"></span> after application</p>

  <p class="abs promise">"We strive to complete work in a professional manner each and every visit. If you are not satisfied with the level of service you are receiving please contact us. We value your business and wish to maintain long-term relationships with our customers. "</p>

  <svg class="abs lawn-band" viewBox="0 0 813 275" preserveAspectRatio="none" aria-hidden="true">
    <defs>
      <linearGradient id="grass" x1="0" y1="0" x2="1" y2="1">
        <stop offset="0" stop-color="#3f9424"/>
        <stop offset=".5" stop-color="#5db533"/>
        <stop offset="1" stop-color="#2f7d1f"/>
      </linearGradient>
      <linearGradient id="sheen" x1="0" y1="0" x2="1" y2="0">
        <stop offset="0" stop-color="#a6de6a" stop-opacity=".2"/>
        <stop offset=".6" stop-color="#a6de6a" stop-opacity=".8"/>
        <stop offset="1" stop-color="#a6de6a" stop-opacity=".3"/>
      </linearGradient>
    </defs>
    <path d="M0 40 C 220 0 520 10 813 30 L813 275 L0 275 Z" fill="url(#grass)"/>
    <path d="M0 170 C 200 110 450 70 813 60 L813 95 C 460 105 240 140 0 215 Z" fill="url(#sheen)"/>
    <path d="M330 275 C 480 180 640 130 813 118 L813 275 Z" fill="#ffffff"/>
    <path d="M330 275 C 480 180 640 130 813 118" fill="none" stroke="#8fd14f" stroke-width="4"/>
  </svg>

  <div class="abs tree-artwork" role="img" aria-label="Illustration of a cluster of leafy green trees"></div>
  <p class="abs brand-name">FENWICK</p>
  <p class="abs brand-tagline">TURF CARE</p>

  <p class="abs contact-phone">604-918-4471</p>
  <p class="abs contact-email">fenwickturfcare@mailora.net</p>

  <div class="abs care-guide">
    <p class="section-title">For best results please follow these general guidelines WATERING YOUR LAWN</p>
    <p class="section-lead">When rainfall is not sufficient to meet your lawns watering needs, follow these guidelines for a lush green lawn</p>
    <ul>
      <li>Your lawn requires approx. 1 - 1.5 inches of water per week, sometimes more in hot dry weather</li>
      <li>Avoid short frequent watering. It is best to water deeply once every 5 - 7 days. This encourages deep root growth.</li>
      <li>You can use a shallow dish or an empty tuna can to measure the amount you have watered. Just place it in the path of the sprinkler and when it is full, move your sprinkler to a new location.</li>
      <li>Aerating your lawn once a year will help your lawn utilize more water and prevent unnecessary runoff</li>
    </ul>
    <p class="section-title">MOWING YOUR LAWN</p>
    <p class="section-lead">Mowing your lawn properly can make all the difference to how it looks throughout the year</p>
    <ul>
      <li>You should mow your lawn at 2.5 - 3 inches (no shorter). Mowing at this length helps shade your roots and provides more leaf surface for your lawn to manufacture its own food. As an added bonus it will help your lawn retain its moisture and reduce watering requirements.</li>
      <li>As a general rule, try not to remove more than 1/3 of the leaves blade in a single mowing. During periods of heavy growth, this may mean mowing more frequently than usual.</li>
      <li>Always ensure your lawn mower is maintained and the blade is sharp so that is cuts cleanly.</li>
      <li>Your last mowing in the fall should be shorter, about 2 inches</li>
    </ul>
  </div>

</div>
</body>
</html>
```